Packaging Design Project for Snack product

we are manufacturer banana chips and potato based snacks.our company name is "tangora Foods" and,looking a packaging design for our new product "Potato Twirls" under brand name " Munvolos".

we need nice colour scheme and wording on the front and back.just a little more professional looking with the wow factor to help it stand out on the shelve.

so pls find below information about the design:
Company name: Tangora Foods
Brand name : Munvolos
Product name : Potato Twirls
Flavored : Sweet & Spicy
Package Size : 40 GM and 100 GM

Target Market(s)

Retail Customers

Industry/Entity Type

It Company

Requirements
Must have
• In this design we need small visible part for display our product.

```html
<!DOCTYPE html>
<html lang="en">
<head>
<meta charset="utf-8">
<title>Munvolos Potato Twirls – Pack Front</title>
<link href="https://fonts.googleapis.com/css2?family=Luckiest+Guy&family=Arimo:wght@700&display=swap" rel="stylesheet">
<style>
  :root {
    --stage-light: #fafafa;
    --stage-dark: #e4e4e4;
    --sky-top: #0f7fc4;
    --sky-bottom: #37b4ea;
    --sky-ray: #0a6aa8;
    --field-light: #d9ea58;
    --field-mid: #9cce3a;
    --field-deep: #2f9a3c;
    --shield-red: #8c1418;
    --shield-edge: #5e0c0f;
    --brand-yellow: #f9c81c;
    --maker-grey: #3b3a36;
    --maker-badge: #4a4843;
    --window-black: #1b1a1a;
    --badge-red: #9b1b20;
    --badge-ring: #c8343a;
    --ribbon-orange: #d8481d;
    --potato-tone: #d8b45a;
    --ink: #111111;
    --white: #ffffff;
  }
  html, body {
    margin: 0;
    width: 1200px;
    height: 1000px;
    overflow: hidden;
  }
  body {
    background: radial-gradient(ellipse at center, var(--stage-light) 40%, var(--stage-dark) 100%);
    position: relative;
  }
  .pack-front {
    position: absolute;
    left: 330px;
    top: 99px;
    width: 540px;
    height: 802px;
    display: block;
  }
  .maker-name {
    font-family: "Arimo", Arial, sans-serif;
    font-weight: 700;
    fill: var(--white);
  }
  .brand-name, .product-name {
    font-family: "Luckiest Guy", "Arial Black", sans-serif;
    fill: var(--brand-yellow);
  }
  .flavour-label, .net-weight {
    font-family: "Arimo", Arial, sans-serif;
    font-weight: 700;
  }
  .flavour-label { fill: var(--white); }
  .net-weight { fill: var(--ink); }
</style>
</head>
<body>
<svg class="pack-front" viewBox="0 0 365 542" xmlns="http://www.w3.org/2000/svg" aria-label="Munvolos Potato Twirls pack front">
  <defs>
    <linearGradient id="sky" x1="0" y1="0" x2="0" y2="1">
      <stop offset="0" stop-color="var(--sky-top)"/>
      <stop offset="1" stop-color="var(--sky-bottom)"/>
    </linearGradient>
    <linearGradient id="field" x1="0" y1="0" x2="0" y2="1">
      <stop offset="0" stop-color="var(--field-light)"/>
      <stop offset="0.55" stop-color="var(--field-mid)"/>
      <stop offset="1" stop-color="var(--field-deep)"/>
    </linearGradient>
    <radialGradient id="potatoes" cx="0.5" cy="0.5" r="0.5">
      <stop offset="0" stop-color="#f0d486"/>
      <stop offset="1" stop-color="var(--potato-tone)"/>
    </radialGradient>
  </defs>

  <!-- sky -->
  <rect class="sky" width="365" height="542" fill="url(#sky)" role="img" aria-label="Blue sunburst sky"/>

  <!-- rolling green fields -->
  <path class="fields" d="M0,150 C110,120 240,170 365,130 L365,542 L0,542 Z" fill="url(#field)" role="img" aria-label="Rolling green striped fields"/>
  <path class="field-band" d="M0,470 C120,440 250,470 365,445 L365,542 L0,542 Z" fill="var(--field-deep)" opacity="0.55"/>

  <!-- maker name on plain oval -->
  <ellipse class="maker-plate" cx="184" cy="54" rx="58" ry="20" fill="var(--maker-badge)"/>
  <text class="maker-name" x="184" y="59" font-size="14" text-anchor="middle" textLength="96" lengthAdjust="spacingAndGlyphs">Tangora Foods</text>

  <!-- title shield -->
  <polygon class="title-shield" points="80,84 290,84 290,176 272,190 185,238 98,190 80,176" fill="var(--shield-red)" stroke="var(--shield-edge)" stroke-width="3"/>

  <!-- brand and product -->
  <text class="brand-name" x="185" y="150" font-size="46" text-anchor="middle" textLength="196" lengthAdjust="spacingAndGlyphs">MUNVOLOS</text>
  <text class="product-name" x="185" y="186" font-size="20" text-anchor="middle" textLength="150" lengthAdjust="spacingAndGlyphs">Potato Twirls</text>

  <!-- product window -->
  <ellipse class="product-window" cx="175" cy="365" rx="155" ry="50" fill="var(--window-black)"/>

  <!-- flavour badge -->
  <g class="flavour-badge">
    <circle cx="297" cy="405" r="46" fill="var(--badge-ring)"/>
    <circle cx="297" cy="405" r="40" fill="var(--badge-red)"/>
    <ellipse cx="294" cy="392" rx="22" ry="16" fill="url(#potatoes)" role="img" aria-label="Whole potatoes"/>
    <rect class="flavour-ribbon" x="240" y="410" width="114" height="22" fill="var(--ribbon-orange)" stroke="var(--white)" stroke-width="1"/>
    <text class="flavour-label" x="297" y="425" font-size="12" text-anchor="middle" textLength="96" lengthAdjust="spacingAndGlyphs">Sweet &amp; Spicy</text>
  </g>

  <!-- net weight -->
  <text class="net-weight" x="316" y="494" font-size="8.5" text-anchor="middle">Net Weight: 100gm</text>
</svg>
</body>
</html>
```